List Now, Launch Later - DL Flyer front & back

Looking for a flyer that has nothing much other than “List Now, Launch Later” on the front with text to fill the back. With image on front that symbolises launch, maybe house being launch like a rocket.
The text has yet to be written but here is the gist: This is for the back of flyer.
List property and delay the launch. In the meantime, we can:
· Prepare contract
· Prepare marketing
· Prepare the property
· Do the Pest and Building Report
· Give the tenants their due notice of sale
· Advise buyers in an off market capacity
This ensures we are first to market when the time comes rather than coming onto the market along with a surge of spring sellers. Buyers are still buying now. The lack of stock is inadvertently creating strength in the market.
The feel has to be modern, clean, contemporary & graphic

```html
<!DOCTYPE html>
<html lang="en">
<head>
<meta charset="utf-8">
<title>List Now, Launch Later – DL Flyer</title>
<link href="https://fonts.googleapis.com/css2?family=Poppins:wght@400;500;600;700&display=swap" rel="stylesheet">
<style>
  :root {
    --stage-blue: #1f6bb1;
    --navy: #06324f;
    --orange: #ef7d00;
    --sky-top: #5e9fdc;
    --sky-mid: #c9def3;
    --sky-light: #eef5fc;
    --grass: #4f9a2e;
    --grass-light: #8cc65a;
    --white: #ffffff;
    --ink: #1d2430;
  }
  * { margin: 0; padding: 0; box-sizing: border-box; }
  html, body {
    width: 1200px; height: 1200px; overflow: hidden;
    background: var(--stage-blue);
    font-family: "Poppins", sans-serif;
  }
  .stage { position: relative; width: 1200px; height: 1200px; }

  .flyer {
    position: absolute; top: 114px; width: 448px; height: 950px; overflow: hidden;
  }
  .flyer--front { left: 104px;
    background: linear-gradient(180deg, var(--sky-top) 0%, var(--sky-mid) 22%, #e9f1f9 55%, #a9cdef 78%, #cfe8f7 90%, #dff0fa 100%);
  }
  .flyer--back { left: 623px;
    background: linear-gradient(180deg, var(--sky-top) 0%, var(--sky-mid) 20%, var(--sky-light) 45%, var(--white) 56%, var(--white) 100%);
  }

  .art-launch-house {
    position: absolute; left: 19px; top: 188px; width: 415px; height: 295px;
    border-radius: 4px;
    background: linear-gradient(180deg, rgba(206,212,222,0) 0%, #cdd2da 18%, #b9bec8 45%, #7ea65c 58%, #4a4a45 63%, rgba(246,200,100,0.55) 75%, rgba(233,241,249,0) 100%);
  }
  .art-grass { position: absolute; left: 0; bottom: 0; width: 448px; height: 108px;
    background: linear-gradient(180deg, rgba(140,198,90,0) 0%, var(--grass-light) 35%, var(--grass) 100%);
  }
  .art-villa { position: absolute; left: 0; bottom: 0; width: 448px; height: 300px;
    background: linear-gradient(180deg, #ffffff 0%, #e9ecef 22%, #c9c3ba 55%, #6fb6c4 78%, #d9dcd8 100%);
  }

  .headline {
    position: absolute; left: 80px; top: 482px; line-height: 1; font-weight: 600;
  }
  .headline__list { display: block; font-size: 176px; color: var(--orange); letter-spacing: -3px; }
  .headline__now { display: block; font-size: 120px; color: var(--navy); font-weight: 700; letter-spacing: -2px; margin-top: -14px; }
  .headline__later { display: block; font-size: 43.5px; color: var(--navy); margin-top: 10px; padding-left: 4px; }

  .back-title {
    position: absolute; left: 0; width: 448px; top: 88px; text-align: center;
    font-size: 40px; font-weight: 600; color: var(--navy); line-height: 58px; letter-spacing: -0.3px;
  }
  .back-band {
    position: absolute; left: 53px; top: 209px; width: 344px; height: 38px;
    background: var(--navy); color: var(--orange);
    font-size: 24px; font-weight: 600; line-height: 38px; text-align: center;
  }
  .checklist { position: absolute; left: 62px; top: 279px; width: 380px; list-style: none; }
  .checklist__item {
    position: relative; padding-left: 34px; font-size: 16.5px; font-weight: 500; color: var(--ink);
    line-height: 21px; margin-bottom: 9.5px;
  }
  .checklist__item svg { position: absolute; left: 0; top: 4px; width: 16px; height: 16px; }
  .back-copy {
    position: absolute; left: 37px; top: 520px; width: 373px;
    font-size: 15.3px; line-height: 25px; color: var(--ink);
  }
  .back-copy__line { display: block; text-align: justify; text-align-last: justify; }
  .back-copy__line--last { text-align: left; text-align-last: left; letter-spacing: -0.3px; }
</style>
</head>
<body>
<div class="stage">

  <section class="flyer flyer--front">
    <div class="art-launch-house" role="img" aria-label="House on a slab of lawn lifting off like a rocket with flames beneath it"></div>

    <h1 class="headline">
      <span class="headline__list">List</span>
      <span class="headline__now">Now,</span>
      <span class="headline__later">Launch Later</span>
    </h1>

    <div class="art-grass" role="img" aria-label="Strip of green grass along the bottom edge"></div>
  </section>

  <section class="flyer flyer--back">
    <h2 class="back-title">List property and<br>delay the launch.</h2>
    <div class="back-band">In the meantime, we can:</div>

    <ul class="checklist">
      <li class="checklist__item"><svg viewBox="0 0 16 16"><rect x="1" y="2.5" width="12" height="12" fill="none" stroke="var(--navy)" stroke-width="2"/><path d="M4 8.5l3 3 8-9" fill="none" stroke="var(--navy)" stroke-width="2.2"/></svg>Prepare contract</li>
      <li class="checklist__item"><svg viewBox="0 0 16 16"><rect x="1" y="2.5" width="12" height="12" fill="none" stroke="var(--navy)" stroke-width="2"/><path d="M4 8.5l3 3 8-9" fill="none" stroke="var(--navy)" stroke-width="2.2"/></svg>Prepare marketing</li>
      <li class="checklist__item"><svg viewBox="0 0 16 16"><rect x="1" y="2.5" width="12" height="12" fill="none" stroke="var(--navy)" stroke-width="2"/><path d="M4 8.5l3 3 8-9" fill="none" stroke="var(--navy)" stroke-width="2.2"/></svg>Prepare the property</li>
      <li class="checklist__item"><svg viewBox="0 0 16 16"><rect x="1" y="2.5" width="12" height="12" fill="none" stroke="var(--navy)" stroke-width="2"/><path d="M4 8.5l3 3 8-9" fill="none" stroke="var(--navy)" stroke-width="2.2"/></svg>Do the Pest and Building Report</li>
      <li class="checklist__item"><svg viewBox="0 0 16 16"><rect x="1" y="2.5" width="12" height="12" fill="none" stroke="var(--navy)" stroke-width="2"/><path d="M4 8.5l3 3 8-9" fill="none" stroke="var(--navy)" stroke-width="2.2"/></svg>Give the tenants their due<br>notice of sale</li>
      <li class="checklist__item"><svg viewBox="0 0 16 16"><rect x="1" y="2.5" width="12" height="12" fill="none" stroke="var(--navy)" stroke-width="2"/><path d="M4 8.5l3 3 8-9" fill="none" stroke="var(--navy)" stroke-width="2.2"/></svg>Advise buyers in an off market capacity</li>
    </ul>

    <p class="back-copy">
      <span class="back-copy__line">This ensures we are first to market when the</span>
      <span class="back-copy__line">time comes rather than coming onto the</span>
      <span class="back-copy__line">market along with a surge of spring sellers.</span>
      <span class="back-copy__line">Buyers are still buying now. The lack of stock is</span>
      <span class="back-copy__line back-copy__line--last">inadvertently creating strength in the market.</span>
    </p>

    <div class="art-villa" role="img" aria-label="Modern white villa with a patio table, umbrella and swimming pool"></div>
  </section>

</div>
</body>
</html>
```